Portfolio Project

The Portfolio gives you the opportunity to “package” your experience, expertise, and testimonials in a professional brochure-like format. This can be used to present in an interview to discuss you as a “product,” similar to what a salesperson would do when they are presenting their product’s features and benefits.
It’s an impressive way to present yourself as a professional who understands the importance of standing out and making an impactful statement about your skills, talents and success.
The components of this project need to include the following:
I. Resume (I have. No need to do anything with this)
II. Top 3 Features to Summarize You (Leadership/Sales/Driven)
a. These should be dividers in your portfolio that easily highlight your “product offerings”
b. Attributes you would use to describe and promote yourself
c. Make this up and i will ad on. Ex: Marketing, Sales, Training, Customer Service, Project Management, etc.
III. Each Feature must incorporate the following behind it – Do this for EACH Feature
a. Summarize experience – provide summary of what you did – make it quantifiable: numbers, charts, graphs
b. Provide examples: any proof of work, design, projects, etc.
c. Provide testimonials: emails of job well done, communications, etc.
d. Provide awards, certifications, recognitions (I Have)
IV. References ( I have)
a. Include at least two reference letters that will highlight your professional/working experience. (i have)
V. Professionally bind the portfolio (I will do)
Updates

I have increased the budget by $50.

Just a reminder, this is a portfolio to give to someone in a job interview. The finished size will be aprox 10 - 15 pages total. It will include a lot of pictures of me and my accomplishments in the military and school. It will Including my resume and scanned photos of awards that I have received (I will do). What I'm needing from a designer is aprox 10 pages that includes a few of the pictures of me with a nice background and layout. Writing about myself and my accomplishments and goals isn't difficult for me. What I need help with is the format/graphics/layout with places to write about myself and my accomplishments. In the Military (Harbor Guard), in the course for mastery in trading (CMT) at College of Brantwick and with pitch right in (my company) www.pitchrightinhub.example it should be fairly easy for a graphic designer. I have uploaded my resume to this website for your viewing.

I have also uploaded an example of a friends personal portfolio to the website. That is one of the better ones I have seen. THIS IS A GOOD REFERENCE. HIS IS VERY GOOD. 

I DO NOT WANT IT TO "BUSY". THE FOCUS IS ON ME AND MY ACCOMPLISHMENTS.

Once I receive the files I will print and get bonded (like a book or magazine). I would like to be able to interchange pictures on the document as well if possible. So if later on I want to use a different picture or a higher quality picture I can. Please feel free to contact me with ANY questions!

rkmalden71@mailbox.example
001 555 014 7392

Thank You.

Target Market(s)

CEO's,VP's, HR managers

Industry/Entity Type

Leadership

Requirements
Must have
• Please see Example attached.
Nice to have
• If you have ANY questions at all please feel free to e-mail me at rkmalden71@mailbox.example

```html
<!DOCTYPE html>
<html lang="en">
<head>
<meta charset="utf-8">
<title>Reid K. Malden — Sales Portfolio Spread</title>
<link rel="stylesheet" href="https://fonts.googleapis.com/css2?family=Cinzel:wght@400;600&family=Fondamento:ital@0;1&family=Lora:ital@1&family=Open+Sans:ital,wght@0,300;0,400;0,600;0,700;1,600&display=swap">
<style>
  :root{
    --stage:#4a3128;
    --navy:#0b1f44;
    --navy-deep:#061634;
    --blue:#1d4e93;
    --blue-mid:#2a5aa8;
    --sky:#38b4ee;
    --ice:#dfe8f3;
    --ice-2:#c9d8ea;
    --card:rgba(120,160,215,.28);
    --red:#c3161c;
    --red-deep:#7c0b10;
    --white:#ffffff;
    --pale:#d3e2f2;
    --ink:#1c2a44;
  }
  *{box-sizing:border-box;margin:0;padding:0}
  html,body{width:1200px;height:862px;overflow:hidden;background:var(--stage)}
  body{position:relative;font-family:"Open Sans",Arial,sans-serif;color:var(--ink)}
  .page{position:absolute;top:42px;width:525px;height:743px;overflow:hidden;box-shadow:0 4px 14px rgba(0,0,0,.45)}
  .page--inner{left:55px;background:var(--navy)}
  .page--cover{left:608px;background:linear-gradient(180deg,var(--navy-deep) 0%,var(--navy) 45%,#0d2a5a 100%)}
  .abs{position:absolute}

  /* inner page: achievements */
  .achievements{left:0;top:0;width:525px;height:183px;background:linear-gradient(135deg,var(--ice) 0%,#f2f6fb 50%,var(--ice-2) 100%);border-top:9px solid var(--blue)}
  .section-title{font-weight:300;color:var(--blue-mid);white-space:nowrap}
  .achievements .section-title{left:28px;top:14px;font-size:28px;line-height:1.2}
  .bullets{list-style:none;font-size:8px;line-height:1.25;color:#2b3650}
  .bullets li{position:relative;padding-left:18px;margin-bottom:6px}
  .bullets li::before{content:"";position:absolute;left:0;top:0;width:10px;height:10px;border-radius:50%;background:radial-gradient(circle at 35% 35%,#6f9be0,var(--blue) 70%)}
  .bullets--main{left:30px;top:64px;width:240px;text-align:justify}
  .bullets--side{left:300px;top:64px;width:215px}
  .bullets--side .pair{display:flex;gap:8px}
  .bullets--side .pair span+span{position:relative;padding-left:16px}
  .bullets--side .pair span+span::before{content:"";position:absolute;left:0;top:0;width:10px;height:10px;border-radius:50%;background:radial-gradient(circle at 35% 35%,#6f9be0,var(--blue) 70%)}
  .bullets--side .highlight{font-style:italic;font-weight:600;font-size:9px;line-height:1.45}

  /* inner page: operations */
  .operations{left:0;top:183px;width:525px;height:362px;background:radial-gradient(ellipse at 40% 55%,#1c4f93 0%,#0e2d62 55%,var(--navy-deep) 100%);border-top:1px solid #4e7fc2}
  .script-title{font-family:"Fondamento",Georgia,serif;color:var(--white);font-weight:400;white-space:nowrap;line-height:1.2}
  .operations .ops-title{left:28px;top:8px;font-size:18px}
  .info-card{background:var(--card);border-radius:7px;color:var(--pale);font-size:8.2px;line-height:1.55;padding:8px 10px}
  .info-card--school{left:22px;top:48px;width:186px;height:102px}
  .info-card--school h3{font-size:10.5px;font-weight:700;line-height:1.25;color:var(--white);margin-bottom:5px}
  .info-card--school p{margin-bottom:6px}
  .info-card--bio{left:214px;top:48px;width:190px;height:102px;font-size:7.8px}
  .portrait{left:410px;top:48px;width:102px;height:100px;border-radius:7px;background:linear-gradient(180deg,#7f9eb5 0%,#8c8a7a 45%,#5a7a3e 100%)}
  .welcome{left:408px;top:176px;width:110px;text-align:center;font-family:"Fondamento",Georgia,serif;font-style:italic;font-size:10px;line-height:1.35;color:var(--white)}
  .work-title{left:28px;top:187px;font-size:20px;font-weight:300;color:var(--white);letter-spacing:.5px;line-height:1.2}
  .work-line{left:28px;top:220px;font-size:10.5px;color:var(--white);white-space:nowrap}
  .course-line{left:28px;top:275px;width:360px;font-size:12.4px;line-height:1.35;color:var(--pale);font-weight:300}
  .operations .rule{left:28px;top:320px;width:380px;height:1px;background:#7da4d8}
  .operations .tagline{left:28px;top:328px;font-size:16px}

  /* inner page: testimonial */
  .testimonial{left:0;top:545px;width:525px;height:160px;background:linear-gradient(135deg,#f1f5fa 0%,var(--ice) 60%,var(--ice-2) 100%)}
  .testimonial .section-title{left:28px;top:8px;font-size:24px;letter-spacing:.5px;line-height:1.2}
  .quote{font-family:"Lora",Georgia,serif;font-style:italic;font-size:9.4px;line-height:1.2;color:#2e3850}
  .quote--plain{left:28px;top:56px;width:225px;text-align:justify;padding-left:18px}
  .quote--plain::before{content:"";position:absolute;left:0;top:1px;width:10px;height:10px;border-radius:50%;background:radial-gradient(circle at 35% 35%,#6f9be0,var(--blue) 70%)}
  .quote--boxed{left:266px;top:14px;width:250px;height:140px;background:#b9d3ee;border-radius:6px;padding:8px 12px 8px 26px}
  .quote--boxed::before{content:"";position:absolute;left:10px;top:10px;width:10px;height:10px;border-radius:50%;background:radial-gradient(circle at 35% 35%,#6f9be0,var(--blue) 70%)}
  .quote cite{display:block;font-style:italic;margin-top:7px}
  .quote--plain cite{text-align:right}
  .quote cite b{font-weight:700}

  /* inner page: footer */
  .contact-bar{left:0;top:705px;width:525px;height:38px;background:linear-gradient(90deg,#2c63b3,var(--blue) 60%,#3d6fb8);display:flex;align-items:center;padding:0 24px;color:var(--white);border-top:2px solid #7ea5d9;white-space:nowrap}
  .contact-bar .name{font-family:"Cinzel",Georgia,serif;font-size:16px;margin-right:38px;flex:none}
  .contact-bar .detail{font-size:7.4px;padding:0 10px;border-left:1px solid rgba(255,255,255,.7);flex:none}
  .contact-bar .detail:first-of-type{border-left:none;position:relative;padding-left:14px}
  .contact-bar .detail:first-of-type::before{content:"";position:absolute;left:0;top:1px;width:9px;height:9px;border-radius:50%;background:radial-gradient(circle at 35% 35%,#8fb3ea,#21488a 70%)}

  /* cover page */
  .cover-name{left:0;top:46px;width:525px;text-align:center;font-family:"Cinzel",Georgia,serif;font-weight:400;font-size:36px;color:var(--pale);letter-spacing:.5px;white-space:nowrap}
  .cover-art{left:0;top:0;width:525px;height:743px}
  .feature-banner{left:112px;top:152px;font-size:21px;font-weight:700;color:var(--navy);white-space:nowrap;line-height:1.2}
  .feature-banner span{font-size:16px;font-weight:400;letter-spacing:.5px}
  .hero-photo{left:0;top:188px;width:292px;height:358px;background:radial-gradient(ellipse at 50% 45%,#3b2a2c 0%,#4a0d12 45%,var(--red-deep) 100%)}
  .hero-statement{left:362px;top:424px;width:160px;text-align:center;font-size:22px;font-weight:300;line-height:1.3;color:var(--white)}
  .program-tab{left:138px;top:559px;font-size:14px;color:var(--navy);letter-spacing:.3px;line-height:1.2;white-space:nowrap}
  .certified{left:30px;top:706px;font-size:24px;font-weight:300;color:var(--pale);letter-spacing:1.5px;line-height:1.1;white-space:nowrap}
  .badge{top:638px;width:91px;height:90px;background:var(--white);border-radius:2px}
  .badge--one{left:198px}
  .badge--two{left:293px}
  .school-mark{left:398px;width:108px;background:var(--white);border-radius:4px;display:flex;align-items:center;justify-content:center;text-align:center;font-weight:600;color:var(--red);line-height:1.1}
  .school-mark--a{top:584px;height:21px;font-size:8px}
  .school-mark--b{top:611px;height:23px;font-size:7.4px}
  .school-mark--c{top:641px;height:38px;font-size:11px}
  .school-mark--d{top:686px;height:38px;font-size:11px}
</style>
</head>
<body>

<section class="page page--inner" aria-label="Sales page two">
  <div class="abs achievements">
    <h2 class="abs section-title">Sales Achievements</h2>
    <ul class="abs bullets bullets--main">
      <li>Handle and managed all features of business, including client service for over 20 clients, sales for all clients, buying, accountings and employing training.</li>
      <li>Responsible for all business operations.</li>
      <li>Department Head for employment, supervision, and payment for detachment cook for 7 months.</li>
      <li>Hired, trained and supervised all employees.</li>
    </ul>
    <ul class="abs bullets bullets--side">
      <li>Minor: Business Sales</li>
      <li class="pair"><span>Bachelor of Arts</span><span>GPA: 3.25</span></li>
      <li class="pair"><span>Customer Service</span><span>Management</span></li>
      <li class="highlight">Course For Mastery in Trading the Nations #1 Sales Program receiving over 180 hrs of LIVE SALES TRAINING.</li>
    </ul>
  </div>

  <div class="abs operations">
    <h2 class="abs script-title ops-title">Business Operations</h2>
    <div class="abs info-card info-card--school">
      <h3>College of Brantwick/<br>Ashdale, Texas</h3>
      <p>Current record holder in number of golf players sold for CB Sales program’s charity tournament.</p>
      <p>Major: Interpersonal Communication</p>
    </div>
    <div class="abs info-card info-card--bio">Rick Malden has been a successful entrepreneur in the Ashdale-Corwin City area for over 30 years. After 33 years of custom remodeling with Northgate Roofing, Siding &amp; Painting Rick felt inspired to help others with the more down to earth personal needs of life.</div>
    <div class="abs portrait" role="img" aria-label="Photo of Reid Malden outdoors"></div>
    <p class="abs welcome">Welcome to Pitch-Right-In services, Ashdale County’s elite concierge service designed to lend a hand to those in need of just about anything!</p>
    <h2 class="abs work-title">WORK EXPERIENCE</h2>
    <p class="abs work-line">Pitch Right In Concierge LLC: Owner/Operator. August 2009 – Current</p>
    <p class="abs course-line">Course For Mastery in Trading the nations #1 sales program receiving over 180 hrs of live sales training.</p>
    <div class="abs rule"></div>
    <p class="abs script-title tagline">A Practical Concierge Service For Ashdale County</p>
  </div>

  <div class="abs testimonial">
    <h2 class="abs section-title">TESTIMONIAL</h2>
    <blockquote class="abs quote quote--plain">Lorem ipsum dolor sit amet, consectetur adipisicing elit, sed do eiusmod tempor incididunt ut labore et dolore magna aliqua. Ut enim ad minim veniam, quis nostrud exercitation ullamco laboris nisi ut aliquip ex ea commodo consequat.
      <cite><b>Namehere,</b> Designation, Company name</cite>
    </blockquote>
    <blockquote class="abs quote quote--boxed">Lorem ipsum dolor sit amet, consectetur adipisicing elit, sed do eiusmod tempor incididunt ut labore et dolore magna aliqua. Ut enim ad minim veniam, quis nostrud exercitation ullamco laboris nisi ut aliquip ex ea commodo consequat. Duis aute irure dolor in reprehenderit in voluptate velit esse cillum dolore eu fugiat nulla pariatur.
      <cite><b>Namehere,</b> Designation<br>Company name</cite>
    </blockquote>
  </div>

  <footer class="abs contact-bar">
    <span class="name">REID K. MALDEN</span>
    <span class="detail">reid@pitchrightinhub.example</span>
    <span class="detail">Ph: (555) 014-7392</span>
    <span class="detail">Ashdale , TX 70011</span>
  </footer>
</section>

<section class="page page--cover" aria-label="Sales page one">
  <div class="abs hero-photo" role="img" aria-label="Portrait of Reid Malden in a dark suit against a red backdrop"></div>
  <svg class="abs cover-art" viewBox="0 0 525 743" aria-hidden="true">
    <rect x="292" y="188" width="233" height="358" fill="#c3161c"/>
    <polygon points="478,188 525,188 525,546 300,546" fill="#1f5eaf"/>
    <polygon points="478,188 525,188 525,546 400,546" fill="#2a6cc0" opacity=".5"/>
    <line x1="474" y1="188" x2="296" y2="546" stroke="#ffffff" stroke-width="3"/>
    <polygon points="78,148 494,148 476,188 56,188" fill="#38b4ee"/>
    <polygon points="112,551 309,551 292,585 95,585" fill="#38b4ee"/>
  </svg>
  <h1 class="abs cover-name">REID K. MALDEN</h1>
  <p class="abs feature-banner">Sales <span>(CMT College of Brantwick)</span></p>
  <p class="abs hero-statement">RESPONSIBLE FOR ALL BUSINESS OPERATIONS</p>
  <p class="abs program-tab">SALES PROGRAM</p>
  <p class="abs certified">Certified in:</p>
  <div class="abs badge badge--one" role="img" aria-label="Certification badge"></div>
  <div class="abs badge badge--two" role="img" aria-label="Certification badge"></div>
  <div class="abs school-mark school-mark--a">COLLEGE OF BRANTWICK</div>
  <div class="abs school-mark school-mark--b">COLLEGE OF BRANTWICK SALES</div>
  <div class="abs school-mark school-mark--c">HALDEN SCHOOL<br>OF BUSINESS</div>
  <div class="abs school-mark school-mark--d">COLLEGE OF<br>BRANTWICK</div>
</section>

</body>
</html>
```